Renowned Chiropractic Clinic needs unique and professional business card

We need a clean and professional looking business card that embodies our core values and stands for excellence. Highest standard of care and trustworthiness is what we want a future patient to connect to the design of the business card.
Ideally we want the design of the business card to be unique in nature and have a close connection to the SPINE as it is the core of what we do in our office - working with peoples spines.

Contact Information for Business Card

Font file is modified Nexa light and Montserrat medium. Colors are #5BC9E1, #666666, and #9dd5eb

On the front we would like to have the logo and the name of the office with an engaging, trustworthy and professional design.
On the back we need an area for our address, phone number and email address (This can be also be in the front).
On the back we would also like the slogan (this is however not a must and can also be on the front).

The HEXAGON (the design from the spine), could be an idea for the design to evolve around - this is however up to your professional creativity!

Requirements
Must have
• I want the design to primarily evolve around the HEXAGON shape and to have as few curves in it as possible. Therefore, making the design as "edgy" and "linear" as possible.

- Logo
- German Address Line (we are moving offices so we do not yet have a physical address so it would have to be a placeholder address for now that can be changed) --> Office Name (Line 1), Streetname (Line 2), Zip Code and Town (Line 3)
- email and phone number field
Nice to have
• Incorporation of the slogan "Kehren Sie Ihren Problemen den Rücken"

Please let your imagination run free :)!!! I am excited to work with you all to create an astonishing business card!

```html
<!DOCTYPE html>
<html lang="de">
<head>
<meta charset="utf-8">
<title>Chiropraxis Axialis – Visitenkarten</title>
<link href="https://fonts.googleapis.com/css2?family=Montserrat:wght@300;400;500&display=swap" rel="stylesheet">
<style>
  :root {
    --brand-blue: #5BC9E1;
    --soft-blue: #9dd5eb;
    --text-grey: #666666;
    --board: #d9dadc;
    --paper: #ffffff;
  }
  html, body { margin: 0; padding: 0; overflow: hidden; }
  body { width: 1008px; height: 1200px; background: var(--board); position: relative; font-family: "Montserrat", sans-serif; }
  .shapes { position: absolute; left: 0; top: 0; width: 1008px; height: 1200px; }
  .t { position: absolute; margin: 0; line-height: 1; white-space: nowrap; }
  .label { font-weight: 300; color: var(--text-grey); letter-spacing: 0.62em; font-size: 11px; }
  .name { font-weight: 300; color: var(--brand-blue); letter-spacing: -0.01em; }
  .slogan { font-weight: 400; color: var(--text-grey); font-size: 14px; letter-spacing: 0.01em; }
  .slogan-small { font-size: 11px; }
  .slogan-stack { font-size: 11px; letter-spacing: 0.18em; text-align: center; line-height: 16.5px; transform: translateX(-50%); }
  .contact { position: absolute; margin: 0; color: var(--text-grey); font-weight: 300; font-size: 14px; line-height: 19px; }
  .contact .row { display: flex; align-items: center; }
  .contact .icon { width: 10px; height: 11px; margin-left: -13px; margin-right: 3px; }
  .contact .gap { height: 12px; }
  .contact-center { position: absolute; margin: 0; color: var(--text-grey); font-weight: 300; font-size: 13px; line-height: 17px; text-align: center; transform: translateX(-50%); }
  .contact-center .gap { height: 8px; }
</style>
</head>
<body>

<svg class="shapes" viewBox="0 0 1008 1200" aria-hidden="false">
  <defs>
    <linearGradient id="honeycomb-tone" x1="0" y1="0" x2="1" y2="0">
      <stop offset="0" stop-color="#9dd5eb" stop-opacity="0"/>
      <stop offset="1" stop-color="#9dd5eb" stop-opacity="0.35"/>
    </linearGradient>
    <linearGradient id="honeycomb-tone-top" x1="0" y1="0" x2="0" y2="1">
      <stop offset="0" stop-color="#9dd5eb" stop-opacity="0.3"/>
      <stop offset="1" stop-color="#9dd5eb" stop-opacity="0"/>
    </linearGradient>
  </defs>

  <!-- card shapes -->
  <rect x="60" y="64" width="433" height="250" fill="#fff"/>
  <rect x="60" y="338" width="433" height="249" fill="#fff"/>
  <rect x="516" y="338" width="433" height="249" fill="#fff"/>
  <polygon points="60,611 423,611 493,736 423,861 60,861" fill="#fff"/>
  <polygon points="516,611 879,611 949,736 879,861 516,861" fill="#fff"/>
  <polygon points="191,885 350,885 420,1010 350,1135 191,1135 133,1010" fill="#fff"/>
  <polygon points="647,885 805,885 876,1010 805,1135 647,1135 589,1010" fill="#fff"/>

  <!-- honeycomb texture areas -->
  <polygon role="img" aria-label="Hexagon-Wabenmuster in Hellblau" points="315,64 493,64 493,241 450,241" fill="url(#honeycomb-tone)"/>
  <polygon role="img" aria-label="Hexagon-Wabenmuster in Hellblau" points="315,338 493,338 493,514 450,514" fill="url(#honeycomb-tone)"/>
  <polygon role="img" aria-label="Hexagon-Wabenmuster in Hellblau" points="760,338 949,338 949,587 760,587" fill="url(#honeycomb-tone)"/>
  <polygon role="img" aria-label="Hexagon-Wabenmuster in Hellblau" points="295,611 423,611 493,736 423,861 370,861 380,736" fill="url(#honeycomb-tone)"/>
  <polygon role="img" aria-label="Hexagon-Wabenmuster in Hellblau" points="750,611 879,611 949,736 879,861 740,861" fill="url(#honeycomb-tone)"/>
  <polygon role="img" aria-label="Hexagon-Wabenmuster in Hellblau" points="191,885 350,885 395,965 180,965" fill="url(#honeycomb-tone-top)"/>
  <polygon role="img" aria-label="Hexagon-Wabenmuster in Hellblau" points="647,885 805,885 845,955 630,955" fill="url(#honeycomb-tone-top)"/>

  <!-- divider with icons on hexagon back -->
  <line x1="660" y1="1020" x2="712" y2="1020" stroke="#9dd5eb" stroke-width="0.8"/>
  <line x1="758" y1="1020" x2="811" y2="1020" stroke="#9dd5eb" stroke-width="0.8"/>
  <rect x="718" y="1016.5" width="9" height="7" fill="#5BC9E1"/>
  <circle cx="735" cy="1020" r="4" fill="#5BC9E1"/>
  <path d="M749 1015.5a3.5 3.5 0 0 1 3.5 3.5c0 2.5-3.5 5.5-3.5 5.5s-3.5-3-3.5-5.5a3.5 3.5 0 0 1 3.5-3.5z" fill="#5BC9E1"/>
</svg>

<!-- Card 1: front -->
<p class="t label" style="left:239px; top:183px;">CHIROPRAXIS</p>
<p class="t name" style="left:217px; top:193px; font-size:54px;">AXIALIS</p>
<p class="t slogan" style="left:107px; top:269px;">KEHREN SIE IHREN PROBLEMEN DEN RÜCKEN</p>

<!-- Card 2: front -->
<p class="t label" style="left:207px; top:424px;">CHIROPRAXIS</p>
<p class="t name" style="left:187px; top:436px; font-size:54px;">AXIALIS</p>
<p class="t slogan" style="left:107px; top:543px;">KEHREN SIE IHREN PROBLEMEN DEN RÜCKEN</p>

<!-- Card 2: back -->
<p class="t label" style="left:566px; top:377px; font-size:10px;">CHIROPRAXIS</p>
<p class="t name" style="left:549px; top:386px; font-size:42px;">AXIALIS</p>
<div class="contact" style="left:569px; top:456px;">
  <div class="row"><svg class="icon" viewBox="0 0 10 11"><path d="M5 0.5a3.5 3.5 0 0 1 3.5 3.5c0 3-3.5 6.5-3.5 6.5S1.5 7 1.5 4A3.5 3.5 0 0 1 5 0.5z" fill="#5BC9E1"/><circle cx="5" cy="4" r="1.3" fill="#fff"/></svg>Office Name</div>
  <div class="row">Streetname</div>
  <div class="row">Zip Code and Town</div>
  <div class="gap"></div>
  <div class="row"><svg class="icon" viewBox="0 0 10 11"><rect x="0" y="2" width="10" height="7.5" fill="#5BC9E1"/><path d="M0 2l5 4 5-4" stroke="#fff" stroke-width="1" fill="none"/></svg>email</div>
  <div class="row"><svg class="icon" viewBox="0 0 10 11"><circle cx="5" cy="5.5" r="5" fill="#5BC9E1"/><path d="M3.5 3c0 3 1.5 4.5 3.5 5" stroke="#fff" stroke-width="1.3" fill="none"/></svg>phone number field</div>
</div>

<!-- Card 3: arrow front -->
<p class="t label" style="left:166px; top:708px;">CHIROPRAXIS</p>
<p class="t name" style="left:146px; top:719px; font-size:50px;">AXIALIS</p>
<p class="t slogan slogan-small" style="left:100px; top:819px;">KEHREN SIE IHREN PROBLEMEN DEN RÜCKEN</p>

<!-- Card 3: arrow back -->
<p class="t label" style="left:566px; top:650px; font-size:10px;">CHIROPRAXIS</p>
<p class="t name" style="left:549px; top:659px; font-size:42px;">AXIALIS</p>
<div class="contact" style="left:569px; top:729px;">
  <div class="row"><svg class="icon" viewBox="0 0 10 11"><path d="M5 0.5a3.5 3.5 0 0 1 3.5 3.5c0 3-3.5 6.5-3.5 6.5S1.5 7 1.5 4A3.5 3.5 0 0 1 5 0.5z" fill="#5BC9E1"/><circle cx="5" cy="4" r="1.3" fill="#fff"/></svg>Office Name</div>
  <div class="row">Streetname</div>
  <div class="row">Zip Code and Town</div>
  <div class="gap"></div>
  <div class="row"><svg class="icon" viewBox="0 0 10 11"><rect x="0" y="2" width="10" height="7.5" fill="#5BC9E1"/><path d="M0 2l5 4 5-4" stroke="#fff" stroke-width="1" fill="none"/></svg>email</div>
  <div class="row"><svg class="icon" viewBox="0 0 10 11"><circle cx="5" cy="5.5" r="5" fill="#5BC9E1"/><path d="M3.5 3c0 3 1.5 4.5 3.5 5" stroke="#fff" stroke-width="1.3" fill="none"/></svg>phone number field</div>
</div>

<!-- Card 4: hexagon front -->
<p class="t label" style="left:228px; top:989px; font-size:8px;">CHIROPRAXIS</p>
<p class="t name" style="left:213px; top:997px; font-size:38px;">AXIALIS</p>
<p class="t slogan slogan-stack" style="left:276px; top:1067px;">KEHREN SIE IHREN<br>PROBLEMEN DEN<br>RÜCKEN</p>

<!-- Card 4: hexagon back -->
<p class="t label" style="left:645px; top:952px; font-size:10px;">CHIROPRAXIS</p>
<p class="t name" style="left:628px; top:961px; font-size:48px;">AXIALIS</p>
<div class="contact-center" style="left:732px; top:1031px;">
  <div>email</div>
  <div>phone number field</div>
  <div class="gap"></div>
  <div>Office Name</div>
  <div>Streetname</div>
  <div>Zip Code and Town</div>
</div>

</body>
</html>
```